Real Estate Business Card Redesign Overall - Modern and Clean

Dear All,
I am a real estate Broker in the Texas,USA that has 2 real estate companies that I own. I wanted a clean ,cool modern look on the front with my name and contact info.

The cards can be white or dark color. I plan on using Fipla Print to prin the card in the Luxe Paper. If you think i should rounded corners , i can do that too.

On the back side I wanted to show both my 2 companies somehow.

TORAMIX is a Commercial Real Estate company

KPH uHomes is a Residential Real Estate Company

Target Market(s)

corporate and luxury markets

Industry/Entity Type

Real Estate

Contact Information for Business Card

Marcus T. Holb
Broker or Principal

Marcus T. Holb | CCIM, CPM®, GRI, SRS

address:
4182 Willow Brank Rd Suite 412
Brenmoor, CO 80917 (you can add USA if you want)

Font styles to use
Other font styles liked:
• arial , avantgarde

Colors
0456a4
6092c4
33b8a4
87cfc6
ffffff
474747
5c5c5c
f78f20
ec1f27

Requirements
Must have
• Marcus T. Holb
• address somewhere
• 4182 Willow Brank Rd Suite 412
• Brenmoor, CO 80917
• office phones 555.304.7122
• fax : 555.304.7123
• mobile 555.871.4409
• i have 2 emails:
• marcus@toramix.example
• marcus@kphuhomes.example
• websites:
• www.toramix.example
• www.kphuhomes.example
Nice to have
• Front of the card can be clean with just my name and contact info
• Modern and clean
• On the back we can split the 2 businesses Commercial and Residential

```html
<!DOCTYPE html>
<html lang="en">
<head>
<meta charset="utf-8">
<title>Marcus T. Holb – Business Card</title>
<link rel="stylesheet" href="https://fonts.googleapis.com/css2?family=Arimo:wght@400;700&display=swap">
<style>
  :root {
    --card-blue: #00aeef;
    --ink-white: #ffffff;
    --backdrop: #dcdddf;
    --card-shadow: rgba(0, 0, 0, 0.18);
  }
  html, body {
    margin: 0;
    padding: 0;
    overflow: hidden;
  }
  .canvas {
    position: relative;
    width: 1200px;
    height: 1101px;
    background: var(--backdrop);
    font-family: "Arimo", Arial, sans-serif;
    color: var(--ink-white);
    overflow: hidden;
  }
  .card {
    position: absolute;
    left: 250px;
    width: 700px;
    height: 400px;
    background: var(--card-blue);
    border-radius: 44px;
    box-shadow: 0 10px 24px var(--card-shadow);
  }
  .card-front { top: 120px; }
  .card-back { top: 580px; }

  /* Front */
  .holder-name {
    position: absolute;
    right: 60px;
    top: 190px;
    margin: 0;
    font-size: 58px;
    font-weight: 700;
    letter-spacing: 1px;
    white-space: nowrap;
  }
  .holder-mobile {
    position: absolute;
    right: 64px;
    top: 272px;
    margin: 0;
    font-size: 24px;
    letter-spacing: 14px;
    white-space: nowrap;
  }

  /* Back */
  .office-line {
    position: absolute;
    right: 48px;
    top: 34px;
    margin: 0;
    font-size: 17px;
  }
  .brands {
    position: absolute;
    left: 48px;
    top: 108px;
    display: flex;
    flex-direction: column;
    gap: 14px;
  }
  .brand {
    display: flex;
    align-items: center;
    gap: 8px;
    font-size: 24px;
    font-weight: 700;
  }
  .brand-mark {
    width: 16px;
    height: 16px;
    background: var(--ink-white);
  }
  .contact-list {
    position: absolute;
    right: 48px;
    top: 108px;
    margin: 0;
    padding: 0;
    list-style: none;
    text-align: right;
    font-size: 17px;
    line-height: 22px;
  }
  .contact-list .spaced { letter-spacing: 2px; }
  .contact-list .gap-before { margin-top: 12px; }
  .address {
    position: absolute;
    left: 0;
    right: 0;
    bottom: 40px;
    margin: 0;
    font-style: normal;
    text-align: center;
    font-size: 17px;
    line-height: 22px;
    letter-spacing: 4px;
  }
</style>
</head>
<body>
<main class="canvas">

  <section class="card card-front" aria-label="Card front">
    <h1 class="holder-name">MARCUS T . HOLB</h1>
    <p class="holder-mobile">555.871.4409</p>
  </section>

  <section class="card card-back" aria-label="Card back">
    <p class="office-line">office phones 555.304.7122</p>

    <div class="brands">
      <div class="brand"><span class="brand-mark"></span>KPH uHomes</div>
      <div class="brand"><span class="brand-mark"></span>TORAMIX</div>
    </div>

    <ul class="contact-list">
      <li>marcus@toramix.example</li>
      <li>marcus@kphuhomes.example</li>
      <li class="spaced">www.toramix.example</li>
      <li class="spaced">www.kphuhomes.example</li>
      <li class="spaced gap-before">Fax : 555.304.7123</li>
      <li class="spaced">Mobile 555.871.4409</li>
    </ul>

    <address class="address">
      4182 Willow Brank Rd Suite 412<br>
      Brenmoor, CO 80917
    </address>
  </section>

</main>
</body>
</html>
```